We perform state of the art Lasik Eye Surgery. We are looking for a promotional postcard - oversize / jumbo to send to prospective patients. Our website is www.harbelclarity.com which we would have the look and feel we would like to match. Typically we would like to illustrate "freedom from glasses and contact lenses". This is often done with action / sports images or images of happy faces.

I am attaching our corporate logo - that could be modified if needed and a head shot of Dr. Marcus Toller. The latter is not necessarily needed on the postcard.

Target Market(s)

Adults in Portland Oregon with discretionary income that wear glasses or contact lenses. Typical age range is 20 to 65ish with mean age 40.

Industry/Entity Type

Promotional

Colors

Designer to choose colors to be used in the design.

Requirements
Must have
• Corporate logo or newly designed similar logo ie. logo can be modified to fit the layout
Nice to have
• Freedom from hassle of glasses / save money on glasses and contact solutions etc / Enjoy sports / Personal reward / Live Life to the Fullest

```html
<!DOCTYPE html>
<html lang="en">
<head>
<meta charset="utf-8">
<title>Harbel Clarity Postcard</title>
<link rel="stylesheet" href="https://fonts.googleapis.com/css2?family=Open+Sans:wght@400;600&display=swap">
<style>
  :root {
    --gold: #c1962f;
    --gold-deep: #b0872a;
    --ink: #111111;
    --paper: #ffffff;
    --stage: #ffffff;
    --edge: #d8d8d8;
    --photo-warm: #d9c3a8;
    --photo-dark: #3c3f49;
    --fade: #ecebe8;
  }
  * { box-sizing: border-box; margin: 0; padding: 0; }
  html, body { width: 900px; height: 1200px; overflow: hidden; background: var(--stage); }
  body { position: relative; font-family: "Open Sans", Arial, sans-serif; }

  .card {
    position: absolute;
    left: 24px;
    width: 852px;
    background: var(--paper);
    border: 1px solid var(--edge);
    box-shadow: 0 2px 6px rgba(0,0,0,0.12);
    overflow: hidden;
  }
  .card--front { top: 24px; height: 552px; }
  .card--back { top: 615px; height: 561px; }

  /* Front */
  .brand {
    position: absolute; left: 22px; top: 18px;
    display: flex; align-items: center; gap: 10px;
  }
  .brand__dot { width: 16px; height: 16px; border-radius: 50%; background: var(--gold); }
  .brand__name { font-size: 26px; font-weight: 600; color: var(--gold); line-height: 1; }
  .brand__tag { position: absolute; left: 48px; top: 58px; font-size: 12px; font-weight: 600; color: var(--gold); }

  .peeker {
    position: absolute;
    background: linear-gradient(180deg, var(--photo-warm), #bfa287);
    border-radius: 40px 40px 6px 6px;
  }
  .card--front .peeker { right: 70px; top: 0; width: 150px; height: 186px; }

  .tagline-band {
    position: absolute; left: 100px; right: 0; top: 108px; height: 36px;
    background: var(--ink); color: var(--paper);
    display: flex; align-items: center; padding-left: 24px;
    font-size: 18px; font-weight: 600;
  }

  .hero-panel {
    position: absolute; left: 0; right: 0; top: 160px; height: 340px;
    background: var(--gold);
  }
  .hero-panel__title {
    position: absolute; left: 0; right: 0; top: 36px;
    text-align: center; color: var(--paper);
    font-size: 30px; font-weight: 400; line-height: 1.3;
  }
  .doctor-portrait {
    position: absolute; left: 355px; top: 150px; width: 156px; height: 140px;
    background: linear-gradient(180deg, #9aa3b3 0%, var(--photo-warm) 45%, var(--photo-dark) 100%);
    border: 3px solid var(--paper);
  }
  .credentials {
    position: absolute; left: 0; right: 0; top: 514px;
    text-align: center; font-size: 15px; color: var(--gold-deep); font-weight: 600;
  }

  /* Back */
  .back-photo {
    position: absolute; inset: 0;
    background: radial-gradient(ellipse at 60% 35%, #dcd8d2 0%, var(--fade) 55%, #f5f4f2 100%);
  }
  .card--back .peeker { left: 210px; top: 60px; width: 110px; height: 96px; }
  .contact-panel {
    position: absolute; left: 84px; top: 141px; width: 352px; height: 300px;
    background: var(--gold); color: var(--paper);
    padding: 34px 26px;
    display: flex; flex-direction: column; gap: 18px;
  }
  .office { font-size: 18px; line-height: 1.55; }
  .office__city { font-weight: 600; }
</style>
</head>
<body>
  <section class="card card--front">
    <div class="brand">
      <span class="brand__dot"></span>
      <span class="brand__name">Harbel Clarity Laser Centers</span>
    </div>
    <div class="brand__tag">Laser Vision Correction Team</div>

    <div class="peeker" role="img" aria-label="Photo of a man in thick glasses peeking over the card edge"></div>

    <div class="tagline-band">Freedom from glasses and contact lenses</div>

    <div class="hero-panel">
      <h1 class="hero-panel__title">Change Your Self-image with LASIK Surgery<br>and Turn Some Heads</h1>
      <div class="doctor-portrait" role="img" aria-label="Head shot of Dr. Marcus Toller"></div>
    </div>

    <p class="credentials">Dr. Marcus Toller Board Certified Ophthalmologist in Portland &amp; Vancouver, WA</p>
  </section>

  <section class="card card--back">
    <div class="back-photo" role="img" aria-label="Faded large portrait of the doctor as background"></div>
    <div class="peeker" role="img" aria-label="Photo of a man in thick glasses peeking over the contact panel"></div>
    <div class="contact-panel">
      <div class="office">
        <p class="office__city">Vancouver, WA</p>
        <p>Toll Free: (555) 014-2290 (2291)</p>
      </div>
      <div class="office">
        <p class="office__city">Beaverton, OR</p>
        <p>Toll Free: (555) 014-2291</p>
      </div>
      <div class="office">
        <p class="office__city">Salem, OR</p>
        <p>Toll Free: (555) 014-2291</p>
      </div>
    </div>
  </section>
</body>
</html>
```